Skin care products for Men Label design

I am looking for a designer, who can help with the label design for my new skin care products line for Men.
Modern design, with a manly feel for ecology products.
Colors that must be included:
Black and Blue (see company logo in uploaded files)

These are the measurements:

Cleanser: MM: 130 x 60

Skintonic : MM:130 x 60

Day Creme: MM 105 x 74

Target Market(s)

Men aged 25-55

Industry/Entity Type

Skin Care Product

Requirements
Must have
• Colors that must be included:

```html
<!DOCTYPE html>
<html lang="en">
<head>
<meta charset="utf-8">
<title>True Summit – Men's Skin Care Labels</title>
<link href="https://fonts.googleapis.com/css2?family=Fira+Sans+Condensed:ital,wght@0,500;0,600;1,400;1,500;1,600&display=swap" rel="stylesheet">
<style>
  :root {
    --page: #f1f1f1;
    --label: #dcdcdc;
    --label-light: #e4e4e4;
    --label-shade: #d2d4d8;
    --brand-blue: #2f6fae;
    --ink: #111111;
  }
  * { box-sizing: border-box; margin: 0; padding: 0; }
  html, body { width: 1200px; height: 800px; overflow: hidden; }
  body {
    background: var(--page);
    font-family: "Fira Sans Condensed", "Arial Narrow", sans-serif;
    color: var(--ink);
    position: relative;
  }
  .label {
    position: absolute;
    background: var(--label);
    overflow: hidden;
    box-shadow: 0 2px 10px rgba(0,0,0,0.08);
  }
  .label__pattern {
    position: absolute;
    inset: 0;
    background: linear-gradient(100deg, var(--label-shade) 0%, var(--label-light) 45%, var(--label) 70%, var(--label-shade) 100%);
  }
  .label__content { position: absolute; inset: 0; }
  .brand {
    position: absolute;
    display: flex;
    align-items: center;
    gap: 6px;
    font-weight: 600;
    font-style: normal;
    color: var(--brand-blue);
    white-space: nowrap;
  }
  .brand__mark { display: inline-block; background: var(--brand-blue); }
  .line-tag { font-style: italic; font-weight: 600; color: var(--brand-blue); letter-spacing: 0.08em; white-space: nowrap; }
  .line-sub { font-style: italic; font-weight: 400; color: var(--ink); letter-spacing: 0.1em; white-space: nowrap; }
  .name-top { font-style: italic; font-weight: 600; color: var(--ink); line-height: 1; white-space: nowrap; }
  .name-mid { font-style: italic; font-weight: 500; color: var(--brand-blue); line-height: 1; white-space: nowrap; }
  .name-bottom { font-style: italic; font-weight: 500; color: var(--ink); letter-spacing: 0.08em; line-height: 1; white-space: nowrap; }
  .net-weight { position: absolute; font-style: italic; font-weight: 500; font-size: 9px; color: var(--ink); white-space: nowrap; }

  /* tall labels: cleanser and tonic, 60 x 130 mm */
  .label--tall { width: 240px; height: 520px; top: 140px; }
  .label--cleanser { left: 80px; }
  .label--tonic { left: 360px; }
  .label--tall .brand { top: 40px; left: 50%; transform: translateX(-50%); font-size: 18px; }
  .label--tall .brand__mark { width: 12px; height: 12px; }
  .label--tall .product-text { position: absolute; left: 44px; top: 180px; }
  .label--tall .line-tag { font-size: 15px; }
  .label--tall .line-sub { font-size: 14px; margin-top: 4px; }
  .label--tall .name-top { font-size: 22px; margin-top: 50px; }
  .label--tall .name-mid { font-size: 34px; }
  .label--tall .name-bottom { font-size: 22px; margin-top: 2px; }
  .label--tall .net-weight { bottom: 26px; left: 50%; transform: translateX(-50%); }

  /* wide label: day creme, 105 x 74 mm */
  .label--creme { width: 500px; height: 352px; left: 640px; top: 224px; }
  .label--creme .brand { top: 150px; left: 40px; font-size: 20px; }
  .label--creme .brand__mark { width: 13px; height: 13px; }
  .label--creme .product-tag { position: absolute; left: 200px; top: 150px; }
  .label--creme .line-tag { font-size: 14px; }
  .label--creme .line-sub { font-size: 13px; margin-top: 2px; }
  .label--creme .product-name { position: absolute; left: 330px; top: 120px; }
  .label--creme .name-top { font-size: 20px; }
  .label--creme .name-mid { font-size: 30px; }
  .label--creme .name-bottom { font-size: 20px; margin-top: 2px; }
  .label--creme .net-weight { bottom: 40px; left: 50%; transform: translateX(-50%); }
</style>
</head>
<body>

  <section class="label label--tall label--cleanser">
    <div class="label__pattern" role="img" aria-label="Soft background pattern of flowing grey and blue lines"></div>
    <div class="label__content">
      <div class="brand"><span class="brand__mark"></span>True Summit</div>
      <div class="product-text">
        <p class="line-tag">FASHION MEN’S</p>
        <p class="line-sub">SKIN CARE</p>
        <p class="name-top">SUPREME</p>
        <p class="name-mid">CALM</p>
        <p class="name-bottom">SKIN EASE</p>
      </div>
      <p class="net-weight">NETWT.1.35OZ/38.27G</p>
    </div>
  </section>

  <section class="label label--tall label--tonic">
    <div class="label__pattern" role="img" aria-label="Soft background pattern of flowing grey and blue lines"></div>
    <div class="label__content">
      <div class="brand"><span class="brand__mark"></span>True Summit</div>
      <div class="product-text">
        <p class="line-tag">FASHION MEN’S</p>
        <p class="line-sub">SKIN CARE</p>
        <p class="name-top">SUPREME</p>
        <p class="name-mid">CALM</p>
        <p class="name-bottom">SKIN EASE</p>
      </div>
      <p class="net-weight">NETWT.1.35OZ/38.27G</p>
    </div>
  </section>

  <section class="label label--creme">
    <div class="label__pattern" role="img" aria-label="Soft background pattern of flowing grey and blue lines"></div>
    <div class="label__content">
      <div class="brand"><span class="brand__mark"></span>True Summit</div>
      <div class="product-tag">
        <p class="line-tag">FASHION MEN’S</p>
        <p class="line-sub">SKIN CARE</p>
      </div>
      <div class="product-name">
        <p class="name-top">SUPREME</p>
        <p class="name-mid">CALM</p>
        <p class="name-bottom">SKIN EASE</p>
      </div>
      <p class="net-weight">NETWT.1.35OZ/38.27G</p>
    </div>
  </section>

</body>
</html>
```